I need a camera ready ad
The specs MUST BE as follows
4.875" wide X 8" TALL 300 DPI

WOULD LIKE TO SEE A VERSION WITH ALL in BLACK AND WHITE AND A VERSION IN COLOR
This ad will be going in a playbill for a play

I would like to see if we can get the logo below included in black and white on the downtown skyline followed by the text included.

Independent Film Production company located in the heart of Ferndale, available for all your video production needs. ​We work with our clientele from pre-production including conception, script writing, storyboarding, casting and talent selection through post production to ensure our client’s goals are brought to life​ with engaging visual content that connects with your audiences​. ​ We pride ourselves on helping artists bring their inspiration to life​. We deliver the highest quality productions while keeping costs low for clients. Contact us for ​narrative ​film, ​documentaries and ​commercial ​production ​services.

Gerald Toskin - Executive Producer/President of Brass Meadow Productions is an ​Independent film producer who is passionate about making a difference through the art of motion picture and helping other artists reach their dreams.

Location
Brass Meadow Productions
47 Marlow street
New York NY 10027
Email: BrassMeadowProductions@quillpost.net
Website: www.BrassMeadowProductions.net

Industry/Entity Type

Artists

Colors
171717
ffffff

```html
<!DOCTYPE html>
<html lang="en">
<head>
<meta charset="utf-8">
<title>Brass Meadow Productions – Playbill Ad</title>
<link rel="stylesheet" href="https://fonts.googleapis.com/css2?family=Roboto+Condensed:ital,wght@0,400;0,500;0,700;1,400&display=swap">
<style>
  :root {
    --ink: #171717;
    --paper: #ffffff;
    --sky-light: #e4e4e4;
    --sky-mid: #9a9a9a;
    --sky-dark: #4a4a4a;
  }
  * { margin: 0; padding: 0; box-sizing: border-box; }
  html, body {
    width: 732px;
    height: 1200px;
    overflow: hidden;
    background: var(--paper);
  }
  .ad {
    position: relative;
    width: 732px;
    height: 1200px;
    background: var(--paper);
    color: var(--ink);
    font-family: "Roboto Condensed", "Arial Narrow", sans-serif;
  }
  .brand {
    position: absolute;
    top: 40px;
    left: 0;
    width: 732px;
    text-align: center;
  }
  .brand-dot {
    display: block;
    width: 96px;
    height: 96px;
    margin: 0 auto 16px;
    border-radius: 50%;
    background: var(--ink);
  }
  .brand-name {
    font-size: 34px;
    font-weight: 500;
    line-height: 1.1;
    color: var(--ink);
  }
  .film-strip {
    position: absolute;
    left: 0;
    width: 732px;
    height: 52px;
    display: block;
  }
  .film-strip--top { top: 220px; }
  .film-strip--bottom { top: 698px; }
  .skyline-photo {
    position: absolute;
    top: 272px;
    left: 0;
    width: 732px;
    height: 426px;
    background:
      linear-gradient(180deg,
        var(--sky-mid) 0%,
        var(--sky-light) 30%,
        var(--sky-light) 48%,
        var(--sky-dark) 55%,
        #2e2e2e 68%,
        #8c8c8c 74%,
        #b5b5b5 86%,
        #6a6a6a 100%);
  }
  .copy {
    position: absolute;
    top: 766px;
    left: 30px;
    width: 672px;
    font-size: 16.6px;
    font-style: italic;
    line-height: 24.5px;
    text-align: justify;
  }
  .copy p + p { margin-top: 10px; }
  .contact {
    position: absolute;
    top: 1028px;
    left: 107px;
  }
  .contact-title {
    font-size: 21px;
    font-weight: 700;
    text-transform: uppercase;
    letter-spacing: 0.2px;
    margin-bottom: 10px;
  }
  .contact-row {
    display: flex;
    align-items: flex-start;
    font-size: 16.5px;
    line-height: 20px;
    margin-bottom: 8px;
  }
  .contact-icon {
    width: 24px;
    height: 24px;
    margin-right: 12px;
    flex: none;
  }
</style>
</head>
<body>
<div class="ad">
  <header class="brand">
    <span class="brand-dot"></span>
    <div class="brand-name">Brass Meadow Productions</div>
  </header>

  <svg class="film-strip film-strip--top" viewBox="0 0 732 52" aria-hidden="true">
    <defs>
      <pattern id="sprocket" x="13" y="0" width="40.2" height="52" patternUnits="userSpaceOnUse">
        <rect x="0" y="10" width="21" height="32" rx="4" fill="#ffffff"/>
      </pattern>
    </defs>
    <rect width="732" height="52" fill="#171717"/>
    <rect x="0" y="0" width="732" height="52" fill="url(#sprocket)"/>
  </svg>

  <div class="skyline-photo" role="img" aria-label="Black and white photo of the downtown city skyline across the river under a cloudy sky"></div>

  <svg class="film-strip film-strip--bottom" viewBox="0 0 732 52" aria-hidden="true">
    <rect width="732" height="52" fill="#171717"/>
    <rect x="0" y="0" width="732" height="52" fill="url(#sprocket)"/>
  </svg>

  <section class="copy">
    <p>Independent Film Production company located in the heart of Ferndale, available for all your video production needs. We work with our clientele from pre-production including conception, script writing, storyboarding, casting and talent selection through post production to ensure our client’s goals are brought to life with engaging visual content that connects with your audiences. We pride ourselves on helping artists bring their inspiration to life. We deliver the highest quality productions while keeping costs low for clients. Contact us for narrative film, documentaries and commercial production services.</p>
    <p>Gerald Toskin - Executive Producer/President of Brass Meadow Productions is an Independent film producer who is passionate about making a difference through the art of motion picture and helping other artists reach their dreams.</p>
  </section>

  <section class="contact">
    <h2 class="contact-title">Brass Meadow Productions</h2>
    <div class="contact-row">
      <svg class="contact-icon" viewBox="0 0 24 24" aria-hidden="true">
        <path d="M12 1C7.6 1 4.5 4.3 4.5 8.4 4.5 14 12 23 12 23s7.5-9 7.5-14.6C19.5 4.3 16.4 1 12 1z" fill="#171717"/>
        <circle cx="12" cy="8.5" r="3" fill="#ffffff"/>
      </svg>
      <span>47 Marlow street<br>New York NY 10027</span>
    </div>
    <div class="contact-row">
      <svg class="contact-icon" viewBox="0 0 24 24" aria-hidden="true">
        <rect x="1" y="5" width="22" height="14" fill="#171717"/>
        <path d="M2 6l10 7 10-7M2 18l7-6M22 18l-7-6" stroke="#ffffff" stroke-width="1.6" fill="none"/>
      </svg>
      <span>BrassMeadowProductions@quillpost.net</span>
    </div>
    <div class="contact-row">
      <svg class="contact-icon" viewBox="0 0 24 24" aria-hidden="true">
        <circle cx="12" cy="12" r="11" fill="#171717"/>
        <circle cx="12" cy="12" r="7" fill="none" stroke="#ffffff" stroke-width="1.4"/>
        <path d="M5 12h14M12 5v14" stroke="#ffffff" stroke-width="1.4"/>
      </svg>
      <span>www.BrassMeadowProductions.net</span>
    </div>
  </section>
</div>
</body>
</html>
```